The Marlowfield Career mentor

The service is premium. It is aimed at people 18-30, so students and those looking to change their first job, principally in the UK but also global. It is offering a very personalised CV writing service and is much more expensive than others on offer. I am very keen that it should look simple and premium. It needs to look very professional, reflecting the aspirational jobs that the clients will be applying for.
If there were three words that summed it up: modern, clean, premium.
I am waiting for all the testimonials to come in but they need to form a major part of the website.
I am also waiting for the full logo design files so that I can upload them. In the meantime there is a copy of the logo.
Thoughts to help those yet to send a design...
This is a premium service and some of the designs have looked very generic. The focus needs to be on quality and the process mentioned in the brief. The partnership and the advantages it brings are crucial but few have mentioned that.

```html
<!DOCTYPE html>
<html lang="en">
<head>
<meta charset="utf-8">
<title>The Marlowfield Career mentor</title>
<link rel="stylesheet" href="https://fonts.googleapis.com/css2?family=Josefin+Sans:wght@400;600;700&family=Prata&display=swap">
<style>
:root{
  --blue:#1a8ff0;
  --ice:#d6f1fc;
  --ink:#1e1e1e;
  --grey:#5d6670;
  --dark:#1b1d22;
  --white:#ffffff;
  --black:#000000;
}
*{box-sizing:border-box;margin:0;padding:0}
html,body{width:1200px;height:5178px;overflow:hidden}
body{position:relative;background:var(--white);font-family:"Josefin Sans",Arial,sans-serif;color:var(--ink)}
.abs{position:absolute}
.heading{font-family:"Prata",Georgia,serif;font-weight:400;text-transform:uppercase;font-size:38px;line-height:52px;color:var(--ink)}
.copy{font-size:13px;line-height:22px;color:var(--grey)}
.btn{position:absolute;height:42px;width:196px;border-radius:6px;background:var(--blue);color:var(--white);font-size:12px;font-weight:700;letter-spacing:1.5px;display:flex;align-items:center;justify-content:center;text-transform:uppercase}
.btn.light{background:var(--white);color:var(--ink);height:40px}
.photo{position:absolute}

/* nav */
.brand{position:absolute;display:flex;align-items:center;gap:10px;color:var(--white);font-size:12px;font-weight:600;letter-spacing:1.5px;line-height:14px;text-transform:uppercase}
.brand .mark{width:12px;height:12px;background:currentColor}
.nav{position:absolute;top:34px;left:392px;font-size:13px;font-weight:700;color:var(--white)}
.nav span{position:absolute;white-space:nowrap}

/* feature cards */
.card{position:absolute;width:232px;background:var(--ice);border-radius:6px;padding:22px 20px 24px}
.card .icon{width:40px;height:40px;background:var(--blue);border-radius:5px;display:flex;align-items:center;justify-content:center;margin-bottom:16px}
.card h3{font-size:14px;font-weight:700;letter-spacing:.6px;line-height:18px;text-transform:uppercase;margin-bottom:12px;color:var(--ink);white-space:nowrap}
.card p{font-size:12px;line-height:19px;color:var(--grey)}

/* testimonials */
.quote{position:absolute;width:222px;background:var(--ice);border-radius:4px;padding:26px 24px}
.quote .qm{font-family:Georgia,serif;font-weight:700;font-size:46px;line-height:30px;height:30px;color:var(--ink)}
.quote p{font-size:10.5px;line-height:17px;color:var(--grey);margin-top:14px}
.quote .who{display:flex;align-items:center;gap:8px;margin-top:16px}
.quote .avatar{width:28px;height:28px;border-radius:50%;background:linear-gradient(135deg,#d9883d,#6b4a3a)}
.quote .who b{display:block;font-size:13px;color:var(--ink);font-weight:700}
.quote .who small{display:block;font-size:11px;color:var(--grey)}

/* blogs */
.blog{position:absolute;top:3970px;width:302px;height:360px;background:var(--ice);border-radius:6px;padding:16px;text-align:center}
.blog .photo{position:relative;height:180px;border-radius:4px}
.blog p{font-size:12px;line-height:19px;color:var(--grey);margin-top:20px;padding:0 8px}
.blog b{display:block;margin-top:14px;font-size:14px;font-weight:700;letter-spacing:.5px}
.blog small{display:block;font-size:11px;color:var(--grey)}
.arrow{position:absolute;width:24px;height:24px;border-radius:50%;background:var(--blue);display:flex;align-items:center;justify-content:center}

/* footer */
.footer{position:absolute;left:0;top:4636px;width:1200px;height:542px;background:var(--black);color:var(--white)}
.fcol{position:absolute;font-size:13px;color:#d0d0d0}
.fcol h4{font-size:13px;font-weight:700;color:var(--white);letter-spacing:.5px;margin-bottom:16px}
.fcol li{list-style:none;height:35px}
.social{position:absolute;display:flex;gap:8px;left:806px}
.social span{width:28px;height:28px;border-radius:50%;background:#8a8a8a}
</style>
</head>
<body>

<!-- HERO -->
<svg class="abs" style="left:0;top:0" width="1200" height="720" viewBox="0 0 1200 720">
  <defs>
    <linearGradient id="heroTone" x1="0" y1="0" x2="1" y2="0.4">
      <stop offset="0" stop-color="#2a2b2f"/>
      <stop offset="0.55" stop-color="#1c1d21"/>
      <stop offset="1" stop-color="#54463c"/>
    </linearGradient>
  </defs>
  <path d="M0,0 H1200 V150 L190,690 Q140,716 112,680 L0,540 Z" fill="#1a8ff0"/>
  <path role="img" aria-label="Photo of a smiling consultant at her desk in a modern office" d="M0,0 H1135 Q1150,20 1120,45 L170,650 Q130,674 104,640 L0,500 Z" fill="url(#heroTone)"/>
</svg>

<div class="brand" style="left:124px;top:24px">
  <span class="mark"></span>
  <span>The Marlowfield<br>Career mentor</span>
</div>
<div class="nav">
  <span style="left:0">Home</span>
  <span style="left:88px">About Us</span>
  <span style="left:203px">What We Offer</span>
  <span style="left:358px">Testimonals</span>
  <span style="left:493px">Blogs</span>
  <span style="left:578px">Contact Us</span>
</div>

<h1 class="heading abs" style="left:124px;top:190px;color:var(--white);font-size:46px;line-height:62px">Professional CVs for<br>your professional<br>future</h1>
<p class="abs" style="left:124px;top:398px;font-size:13px;line-height:24px;color:var(--white)">If so then invest in a CV writing partnership with Oliver, the<br>Marlowfield career mentor.</p>
<div class="btn" style="left:124px;top:474px">Read More</div>

<!-- WHAT WE OFFER -->
<h2 class="heading abs" style="left:124px;top:818px">What We Offer</h2>
<p class="copy abs" style="left:124px;top:890px;width:380px">Lorem Ipsum is simply dummy text of the printing and typesetting industry. Lorem Ipsum has been the industry's standard dummy text ever since the 1500s,hen an unknown printer took a galley of type and scrambled it to make a type specimen book.</p>
<div class="btn" style="left:124px;top:1033px">Read More</div>

<div class="card" style="left:588px;top:816px;min-height:256px">
  <div class="icon"><svg width="22" height="22" viewBox="0 0 22 22" fill="none" stroke="#fff" stroke-width="1.8"><rect x="4" y="3" width="14" height="16" rx="1.5"/><path d="M7 8h8M7 11h8M7 14h5"/></svg></div>
  <h3>Personalised CV<br>Writing</h3>
  <p>Lorem Ipsum is simply dummy text of the printing and typesetting industry. Lorem Ipsum has been the industry's standard dummy text ever since the 1500s.</p>
</div>
<div class="card" style="left:842px;top:730px;min-height:256px">
  <div class="icon"><svg width="22" height="22" viewBox="0 0 22 22" fill="none" stroke="#fff" stroke-width="1.8"><circle cx="11" cy="6" r="3"/><path d="M5 19v-3a6 6 0 0 1 12 0v3M11 12v7"/></svg></div>
  <h3>Aspirational<br>Jobs</h3>
  <p>Lorem Ipsum is simply dummy text of the printing and typesetting industry. Lorem Ipsum has been the industry's standard dummy text ever since the 1500s.</p>
</div>

<!-- PASSIONATE -->
<div class="photo" role="img" aria-label="Dim photo of a modern open-plan office" style="left:16px;top:1170px;width:1168px;height:528px;background:linear-gradient(100deg,#22262b 0%,#2d3238 50%,#1b1e22 100%)"></div>
<div class="abs" style="left:160px;top:1305px;width:326px;height:290px;background:var(--blue);border-radius:10px"></div>
<div class="photo" role="img" aria-label="Photo of a young man giving a thumbs up while a consultant shows him his CV" style="left:124px;top:1274px;width:328px;height:290px;border-radius:12px;background:linear-gradient(135deg,#cfd6dc 0%,#9aa4ad 55%,#2f3f66 100%)"></div>
<h2 class="heading abs" style="left:588px;top:1278px;color:var(--white)">Passionate about<br>your success</h2>
<p class="abs" style="left:588px;top:1402px;width:430px;font-size:13px;line-height:23px;color:var(--white)">People I work with get a job sooner and get a higher paid job. Working with me is personalised, it's a partnership. Together we will build a good CV that will present you in the best way possible, it will increase the chances of you securing the job you want.</p>
<div class="btn light" style="left:588px;top:1548px">Read More</div>

<!-- PARTNERS -->
<h2 class="heading abs" style="left:124px;top:1788px">Your partners in<br>career growth</h2>
<p class="copy abs" style="left:124px;top:1908px;width:330px;line-height:25px">And you'll also get this. As a result of my approach everyone I've worked with is better prepared for interview. Our partnership will</p>
<div class="btn" style="left:124px;top:2040px">Read More</div>
<div class="photo" role="img" aria-label="Illustration of a blue paper plane trailing a dotted flight path" style="left:230px;top:2086px;width:300px;height:262px;border-radius:8px;background:linear-gradient(135deg,#ffffff 0%,#eaf5fd 55%,#cfe6fa 100%)"></div>

<div class="card" style="left:588px;top:1948px;min-height:204px">
  <div class="icon"><svg width="22" height="22" viewBox="0 0 22 22" fill="none" stroke="#fff" stroke-width="1.8"><circle cx="11" cy="6" r="3"/><path d="M4 19h14M7 19v-6h8v6"/></svg></div>
  <h3>Improve<br>Presentation Skills</h3>
  <p>Lorem Ipsum is simply dummy text of the printing and typesetting industry. Lorem Ipsum has been the industry's standard dummy text ever since the 1500s.</p>
</div>
<div class="card" style="left:842px;top:1790px;min-height:258px">
  <div class="icon"><svg width="22" height="22" viewBox="0 0 22 22" fill="none" stroke="#fff" stroke-width="1.8"><rect x="3" y="4" width="16" height="13" rx="1.5"/><circle cx="9" cy="10" r="2.5"/><path d="M13 13l3-3"/></svg></div>
  <h3>Increase Self<br>Awareness</h3>
  <p>Lorem Ipsum is simply dummy text of the printing and typesetting industry. Lorem Ipsum has been the industry's standard dummy text ever since the 1500s.</p>
</div>
<div class="card" style="left:842px;top:2088px;min-height:258px">
  <div class="icon"><svg width="22" height="22" viewBox="0 0 22 22" fill="none" stroke="#fff" stroke-width="1.8"><circle cx="7" cy="8" r="2.5"/><circle cx="15" cy="8" r="2.5"/><path d="M3 17a4 4 0 0 1 8 0M11 17a4 4 0 0 1 8 0"/></svg></div>
  <h3>Build the right sort<br>of confidence</h3>
  <p>Lorem Ipsum is simply dummy text of the printing and typesetting industry. Lorem Ipsum has been the industry's standard dummy text ever since the 1500s.</p>
</div>

<!-- OUR PARTNERSHIP -->
<div class="photo" role="img" aria-label="Photo of a young woman working on a laptop in a modern office" style="left:16px;top:2446px;width:1168px;height:530px;background:linear-gradient(90deg,#4a4038 0%,#2e2b2a 35%,#1f2226 65%,#181a1e 100%)"></div>
<h2 class="heading abs" style="left:572px;top:2532px;color:var(--white)">Our Partnership</h2>
<p class="abs" style="left:572px;top:2600px;width:500px;font-size:14px;line-height:25px;color:var(--white)">The key to all this success is the partnership. Over four sessions we will, together, build a CV. You will get me, no one else, working with you for four sessions. There is a formula for success but it's not formulaic. Your CV will be personal, you will shine through. Your CV will be elevated above the crowd. I offer a premium service, very different to other offerings - so if like those in the testimonials, you get that job sooner, get a higher paid job, the investment is a wise one.</p>
<div class="btn light" style="left:572px;top:2834px">Read More</div>

<!-- TESTIMONIALS -->
<h2 class="heading abs" style="left:124px;top:3066px">What people say<br>about us</h2>
<p class="copy abs" style="left:124px;top:3196px;width:390px">Lorem Ipsum is simply dummy text of the printing and typesetting industry. Lorem Ipsum has been the industry's standard dummy text.</p>

<svg class="abs" style="left:850px;top:3080px" width="22" height="22"><path d="M22,0 V22 H0 A22,22 0 0 1 22,0 Z" fill="#f0506e"/></svg>
<svg class="abs" style="left:328px;top:3356px" width="18" height="18"><path d="M0,0 H18 V18 A18,18 0 0 1 0,0 Z" fill="#f6cf6a"/></svg>
<svg class="abs" style="left:568px;top:3640px" width="20" height="20"><path d="M0,0 H20 A20,20 0 0 1 0,20 Z" fill="#4a56b8"/></svg>

<div class="quote" style="left:124px;top:3388px;height:306px">
  <div class="qm">&#8221;</div>
  <p>Lorem Ipsum is simply dummy text of the printing and typesetting industry. Lorem Ipsum has been the industry's standard dummy text ever since the 1500s,when an unknown printer took a galley of type and scrambled it when an unknown printer.</p>
  <div class="who"><span class="avatar"></span><span><b>Tony</b><small>Lorem Ipsum</small></span></div>
</div>
<div class="quote" style="left:366px;top:3322px;height:306px">
  <div class="qm">&#8221;</div>
  <p>Lorem Ipsum is simply dummy text of the printing and typesetting industry. Lorem Ipsum has been the industry's standard dummy text ever since the 1500s,when an unknown printer took a galley of type and scrambled it when an unknown printer.</p>
  <div class="who"><span class="avatar"></span><span><b>Marcus</b><small>Lorem Ipsum</small></span></div>
</div>
<div class="quote" style="left:610px;top:3070px;height:316px">
  <div class="qm">&#8221;</div>
  <p>Lorem Ipsum is simply dummy text of the printing and typesetting industry. Lorem Ipsum has been the industry's standard dummy text ever since the 1500s,when an unknown printer took a galley of type and scrambled it when an unknown printer.</p>
  <div class="who"><span class="avatar"></span><span><b>Diane</b><small>Lorem Ipsum</small></span></div>
</div>
<div class="quote" style="left:610px;top:3408px;height:312px">
  <div class="qm">&#8221;</div>
  <p>Lorem Ipsum is simply dummy text of the printing and typesetting industry. Lorem Ipsum has been the industry's standard dummy text ever since the 1500s,when an unknown printer took a galley of type and scrambled it when an unknown printer.</p>
  <div class="who"><span class="avatar"></span><span><b>John Doe</b><small>Lorem Ipsum</small></span></div>
</div>
<div class="quote" style="left:852px;top:3122px;height:314px">
  <div class="qm">&#8221;</div>
  <p>Lorem Ipsum is simply dummy text of the printing and typesetting industry. Lorem Ipsum has been the industry's standard dummy text ever since the 1500s,when an unknown printer took a galley of type and scrambled it when an unknown printer.</p>
  <div class="who"><span class="avatar"></span><span><b>Michael</b><small>Lorem Ipsum</small></span></div>
</div>
<div class="quote" style="left:852px;top:3460px;height:318px">
  <div class="qm">&#8221;</div>
  <p>Lorem Ipsum is simply dummy text of the printing and typesetting industry. Lorem Ipsum has been the industry's standard dummy text ever since the 1500s,when an unknown printer took a galley of type and scrambled it when an unknown printer.</p>
  <div class="who"><span class="avatar"></span><span><b>Allison</b><small>Lorem Ipsum</small></span></div>
</div>

<!-- BLOGS -->
<div class="abs" style="left:0;top:3870px;width:82px;height:540px;background:var(--blue);border-radius:0 6px 6px 0"></div>
<div class="abs" style="left:1116px;top:3870px;width:84px;height:540px;background:var(--blue);border-radius:6px 0 0 6px"></div>
<h2 class="heading abs" style="left:0;top:3870px;width:1200px;text-align:center;font-size:40px">Our Blogs</h2>

<div class="blog" style="left:124px">
  <div class="photo" role="img" aria-label="Photo of two businessmen in masks talking at an office table" style="background:linear-gradient(135deg,#9fb4c6,#3e4f66 60%,#2a3345)"></div>
  <p>Lorem Ipsum is simply dummy text of the printing and typesetting industry. Lorem Ipsum has been the industry's standard dummy text ever since the 1500s.</p>
  <b>Michael</b><small>Lorem Ipsum</small>
</div>
<div class="blog" style="left:448px">
  <div class="photo" role="img" aria-label="Photo of colleagues playing chess at a desk in a bright office" style="background:linear-gradient(135deg,#d9b08c,#8a5a3c 55%,#4a3428)"></div>
  <p>Lorem Ipsum is simply dummy text of the printing and typesetting industry. Lorem Ipsum has been the industry's standard dummy text ever since the 1500s.</p>
  <b>Marcus</b><small>Lorem Ipsum</small>
</div>
<div class="blog" style="left:772px">
  <div class="photo" role="img" aria-label="Photo of a business team meeting in a bright office" style="background:linear-gradient(135deg,#e8ecef,#9ea9b3 55%,#4d5761)"></div>
  <p>Lorem Ipsum is simply dummy text of the printing and typesetting industry. Lorem Ipsum has been the industry's standard dummy text ever since the 1500s.</p>
  <b>Tony</b><small>Lorem Ipsum</small>
</div>
<div class="arrow" style="left:102px;top:4150px"><svg width="10" height="10" viewBox="0 0 10 10"><path d="M6.5 1.5L3 5l3.5 3.5" fill="none" stroke="#fff" stroke-width="1.8"/></svg></div>
<div class="arrow" style="left:1074px;top:4150px"><svg width="10" height="10" viewBox="0 0 10 10"><path d="M3.5 1.5L7 5l-3.5 3.5" fill="none" stroke="#fff" stroke-width="1.8"/></svg></div>
<div class="btn" style="left:522px;top:4370px;width:154px;height:38px">See All</div>

<!-- FOOTER -->
<footer class="footer"></footer>
<div class="abs" style="left:124px;top:4508px;width:952px;height:252px;background:var(--ice)"></div>
<p class="abs" style="left:124px;top:4552px;width:952px;text-align:center;font-size:33px;line-height:46px;font-weight:700;letter-spacing:2.5px;color:#3c3c3c;text-transform:uppercase">So take the first step to the best<br>CV you can have.</p>
<div class="btn" style="left:500px;top:4680px;width:198px;height:40px">Contact Us</div>

<div class="brand" style="left:124px;top:4870px">
  <span class="mark"></span>
  <span>The Marlowfield<br>Career mentor</span>
</div>
<p class="abs" style="left:124px;top:4940px;font-size:14px;line-height:28px;color:var(--white)"><b>Phone:</b> 020-7946-0318<br><b>Email:</b> hello@marlowfieldmentor.co.uk</p>

<div class="fcol" style="left:406px;top:4858px">
  <h4>Quick Links</h4>
  <ul><li>Home</li><li>About Us</li><li>What We Offer</li><li>Testimonials</li><li>Blogs</li><li>Contact Us</li></ul>
</div>
<div class="fcol" style="left:574px;top:4858px">
  <h4>Our Services</h4>
  <ul><li>Personalised CV Writing</li><li>Aspirational Jobs</li></ul>
</div>
<div class="fcol" style="left:806px;top:4858px;width:270px">
  <h4>Our Newsletter</h4>
  <p style="line-height:18px">Lorem Ipsum Is Simply Dummy Text Of The Printing And Typesetting Industry.</p>
</div>
<div class="abs" style="left:806px;top:4962px;width:188px;height:38px;background:var(--white);font-size:12px;color:#777;padding:14px 12px">Email Address...</div>
<div class="abs" style="left:994px;top:4962px;width:82px;height:38px;background:var(--blue);color:var(--white);font-size:12px;font-weight:700;display:flex;align-items:center;justify-content:center">Subscribe</div>
<div class="social" style="top:5020px"><span></span><span></span><span></span><span></span><span></span></div>

</body>
</html>
```